Design a Website Mockup (PSD) for a startup legal business

Need designs for a new Immigration law business.

We have already sketched the home page layout. This can be found here:
https://draftlyboard.com/s/8QRT2Lm

A logo needs to be created based on a World Map with Latitude and Longitude lines. It can be any colour, to fit in with your design and colour palette.

Examples of maps can be found here: https://www.plumoraart.com/vector-art/51928-world-map-with-latitude-and-longitude

The greyed area below the menu bar, is for a full-width slider. The mock-up should show a design for the first slider.

The next 2 sections show key topics covered by the business. NOTE: we have placed a phone icon as a placeholder only BUT these need to be replaced, with icons that represent the titles shown.

Colour pallet, design elements and imagery should be based on the American flag, US Passports, the colour metallic gold but we are happy to see alternatives.

Two website Mockup are required, one in standard browser width and the second, “Responsive” showing how the design works on mobile devices.

The project deliverables need to include, final designs for Homepage & Article pages in layered psd format.

```html
<!DOCTYPE html>
<html lang="en">
<head>
<meta charset="utf-8">
<title>Meridian Bridge Consultants</title>
<link href="https://fonts.googleapis.com/css2?family=Poppins:wght@300;400;500;600&display=swap" rel="stylesheet">
<style>
:root{
  --navy:#2c2868;
  --red:#c1272d;
  --ink:#2b2b2b;
  --muted:#8a8a8a;
  --line:#e4e4e4;
  --soft:#f6f7fb;
  --footer:#232323;
  --footer-base:#1b1b1b;
  --white:#fff;
}
*{box-sizing:border-box;margin:0;padding:0}
html,body{width:1200px;height:2860px;overflow:hidden}
body{font-family:'Poppins',sans-serif;color:var(--ink);background:var(--white);position:relative}
.wrap{width:900px;margin:0 auto;position:relative}
section,header,footer{position:relative;width:1200px}

/* top bar */
.topbar{height:30px;border-bottom:1px solid var(--line);font-size:11px;color:var(--muted)}
.topbar .wrap{display:flex;align-items:center;height:30px;gap:14px}
.topbar .ask{color:var(--red)}
.topbar .social{margin-left:auto;display:flex;gap:4px}
.topbar .social span{width:18px;height:18px;border-radius:50%;background:#3b6fb6}
.topbar .social span:last-child{background:var(--red)}
.ticon{display:inline-flex;align-items:center;gap:5px}

/* nav */
.nav{height:62px;box-shadow:0 2px 4px rgba(0,0,0,.05)}
.nav .wrap{display:flex;align-items:center;height:62px}
.brand{display:flex;align-items:center;gap:8px}
.brand-dot{width:38px;height:38px;border-radius:50%;background:#d9dbe2}
.brand-name{font-size:16px;font-weight:500;color:var(--navy);line-height:1.05}
.menu{margin-left:auto;display:flex;gap:42px;font-size:12px;color:#555;letter-spacing:.3px;align-items:center}
.menu .active{color:var(--red)}

/* hero */
.hero{height:375px;background:radial-gradient(ellipse at 45% 55%,#6b4a3c 0%,#3c2a26 45%,#1e1a1c 100%);text-align:center;color:var(--white)}
.hero-title{padding-top:100px;font-size:38px;font-weight:500;letter-spacing:1.5px;line-height:48px}
.hero-title em{font-style:normal;color:var(--red)}
.btn-hero{display:inline-flex;gap:10px;align-items:center;margin-top:14px;background:var(--navy);padding:10px 22px;font-size:15px;letter-spacing:1px}
.dots{position:absolute;left:0;right:0;top:348px;display:flex;justify-content:center;gap:5px}
.dots span{width:8px;height:8px;border-radius:50%;background:var(--white)}
.dots span:nth-child(2){background:var(--red)}

/* section heads */
.sec-head{text-align:center}
.sec-head h2{font-size:27px;font-weight:400;letter-spacing:1.2px;color:#333}
.sec-head p{font-size:11px;color:var(--muted);margin-top:4px}
.sec-head .bar{width:113px;height:3px;background:var(--navy);margin:14px auto 0}

/* advocates */
.advocates{height:423px;padding-top:40px}
.topic-grid{display:grid;grid-template-columns:repeat(3,285px);gap:17px 22px;margin-top:28px}
.topic{height:120px;border:1px solid var(--line);padding:14px 10px 0 62px;position:relative}
.topic.on{border-bottom:3px solid var(--red);box-shadow:0 3px 8px rgba(0,0,0,.08)}
.topic .ico{position:absolute;left:10px;top:15px;width:42px;height:42px;border-radius:50%;border:1px solid var(--line);display:flex;align-items:center;justify-content:center}
.topic.on .ico{background:var(--navy);border-color:var(--navy)}
.topic h3{font-size:14px;font-weight:400;letter-spacing:.3px}
.topic p{font-size:10.5px;color:var(--muted);line-height:16.5px;margin-top:4px}

/* advise */
.advise{height:490px;background:var(--soft);padding-top:40px}
.need-grid{display:grid;grid-template-columns:repeat(3,285px);gap:20px 22px;margin-top:29px}
.need{height:150px;background:var(--white);text-align:center;padding:12px 14px 0}
.need.on{border-bottom:3px solid var(--red);box-shadow:0 4px 12px rgba(0,0,0,.12)}
.need svg{display:block;margin:0 auto}
.need h3{font-size:13px;font-weight:400;margin-top:8px}
.need p{font-size:10.5px;color:var(--muted);line-height:16.5px;margin-top:3px}

/* feature band */
.feature{height:345px;background:var(--navy);overflow:hidden}
.feature-photo{position:absolute;left:0;top:0;width:620px;height:345px;background:linear-gradient(90deg,#9aa6b8 0%,#c7ccd6 40%,#a58ca0 75%,var(--navy) 100%)}
.feature-text{position:absolute;left:614px;top:52px;width:440px;color:var(--white)}
.feature-text h2{font-size:27px;font-weight:400;letter-spacing:1px;display:inline-block;border-bottom:2px solid var(--white);padding-bottom:2px}
.feature-text p{font-size:11px;line-height:16.5px;margin-top:10px;opacity:.9}
.feature-text p + p{margin-top:8px;opacity:1}
.btn-white{display:inline-block;background:var(--white);color:var(--navy);font-size:11px;padding:9px 26px;margin-top:22px}

/* testimonials */
.testimonials{height:339px;background:linear-gradient(180deg,#fafafc,#f3f4f8);padding-top:42px}
.quote{width:680px;margin:30px auto 0;text-align:center;font-size:12px;color:#666;line-height:19.5px;position:relative}
.qmark{position:absolute;top:14px;font-size:40px;color:#c9c9c9;font-family:Georgia,serif}
.arrow{position:absolute;top:218px}
.author{display:flex;align-items:center;justify-content:center;gap:16px;margin-top:24px;margin-right:60px}
.avatar{width:92px;height:92px;border-radius:50%;border:3px solid #e7b4b2;background:#9a9a9a}
.author h4{font-size:14px;font-weight:400;color:var(--navy)}
.author span{font-size:11px;color:var(--muted)}

/* blogs */
.blogs{height:451px;padding-top:40px}
.blog-grid{display:grid;grid-template-columns:repeat(3,283px);gap:26px;margin-top:33px;margin-left:7px}
.post{position:relative}
.post-img{height:179px}
.post-date{position:absolute;left:-7px;top:131px;width:34px;height:48px;background:var(--red);color:var(--white);text-align:center;font-size:20px;line-height:22px;padding-top:5px}
.post-date small{display:block;font-size:8px;line-height:10px}
.post h3{font-size:15px;font-weight:400;margin-top:22px}
.meta{display:flex;gap:16px;font-size:10.5px;color:var(--muted);margin-top:3px}
.meta span{display:inline-flex;align-items:center;gap:5px}
.post p{font-size:11px;color:var(--muted);line-height:17px;margin-top:3px;border-bottom:1px solid var(--line);padding-bottom:10px}

/* footer */
.site-footer{height:300px;background:var(--footer);color:#c8c8c8}
.fcol{position:absolute;top:42px}
.fcol h4{font-size:13.5px;font-weight:400;color:var(--white);letter-spacing:.3px}
.fcol .rule{width:50px;height:2px;background:var(--red);margin:10px 0 22px}
.fcol p{font-size:10px;line-height:15px;text-align:justify}
.links{list-style:none;font-size:10px;line-height:18.7px}
.links li::before{content:"› ";color:#999}
.contact{font-size:10px;display:grid;grid-template-columns:53px 125px;row-gap:0}
.contact dt,.contact dd{padding:8px 0;border-bottom:1px solid #3a3a3a;line-height:16px}
.follow{display:flex;gap:5px;align-items:center}
.follow span{width:11px;height:11px;background:#666}
.follow span:nth-child(2){background:var(--white)}
.field{width:203px;height:28px;border:1px solid #444;margin-bottom:10px;display:flex;align-items:center;gap:7px;padding-left:8px;font-size:9.5px}
.field.msg{height:55px}
.btn-send{display:inline-block;background:var(--navy);color:#ddd;font-size:10px;padding:7px 20px;margin-top:7px}
.totop{position:absolute;right:0;top:176px;width:37px;height:37px;background:#111;display:flex;align-items:center;justify-content:center}
.base{height:45px;background:var(--footer-base);color:#888;font-size:10.5px;text-align:center;line-height:45px}
</style>
</head>
<body>

<header class="topbar">
  <div class="wrap">
    <span class="ticon"><svg width="14" height="10" viewBox="0 0 14 10" fill="none" stroke="#999"><rect x=".5" y=".5" width="13" height="9"/><path d="M.5 .5 7 6l6.5-5.5"/></svg>me@mbc.email</span>
    <span class="ticon"><svg width="11" height="11" viewBox="0 0 24 24" fill="none" stroke="#999" stroke-width="2"><path d="M5 3h4l2 5-3 2a11 11 0 0 0 6 6l2-3 5 2v4a2 2 0 0 1-2 2A17 17 0 0 1 3 5a2 2 0 0 1 2-2z"/></svg><span class="ask">Have any questions?</span> Phone: + 555 014 2200</span>
    <div class="social"><span></span><span></span><span></span><span></span></div>
  </div>
</header>

<nav class="nav">
  <div class="wrap">
    <div class="brand"><span class="brand-dot"></span><span class="brand-name">Meridian Bridge<br>Consultants</span></div>
    <div class="menu">
      <span class="active">HOME</span><span>ABOUT US</span><span>OUR SPECIALITY</span><span>EB-5 VISA</span><span>CONTACT US</span>
      <svg width="14" height="14" viewBox="0 0 14 14" fill="none" stroke="#777" stroke-width="1.4"><circle cx="6" cy="6" r="4.5"/><path d="M9.5 9.5 13 13"/></svg>
    </div>
  </div>
</nav>

<section class="hero" role="img" aria-label="Judge's gavel resting on law books in warm light">
  <h1 class="hero-title">WE UNIQUELY PROTECT <em>YOU</em><br>IN AN INVESTMENT OR DEAL</h1>
  <span class="btn-hero">READ MORE <svg width="14" height="10" viewBox="0 0 14 10" fill="none" stroke="#fff" stroke-width="1.5"><path d="M0 5h12M8 1l4 4-4 4"/></svg></span>
  <div class="dots"><span></span><span></span><span></span></div>
</section>

<section class="advocates">
  <div class="wrap">
    <div class="sec-head"><h2>WE ARE YOUR ADVOCATES WHEN DEALING WITH</h2><p>Lorem Ipsum is simply dummy text of the printing and typesetting industry.</p><div class="bar"></div></div>
    <div class="topic-grid">
      <div class="topic on"><div class="ico"><svg width="22" height="22" viewBox="0 0 24 24" fill="none" stroke="#fff" stroke-width="1.4"><circle cx="12" cy="12" r="9"/><path d="M3 12h18M12 3c3 3 3 15 0 18M12 3c-3 3-3 15 0 18"/></svg></div><h3>A BUSINESS IN THE USA</h3><p>Lorem Ipsum is simply dummy text of the printing and typesetting industry. Lorem Ipsum has been the industry's standard dummy text ever since the 1500s.</p></div>
      <div class="topic"><div class="ico"><svg width="22" height="22" viewBox="0 0 24 24" fill="none" stroke="#999" stroke-width="1.2"><path d="M3 10l5-4 4 3 4-3 5 4-9 8z"/><path d="M8 12l4 3 4-3"/></svg></div><h3>FRANCHISES</h3><p>Lorem Ipsum is simply dummy text of the printing and typesetting industry. Lorem Ipsum has been the industry's standard dummy text ever since the 1500s.</p></div>
      <div class="topic"><div class="ico"><svg width="22" height="22" viewBox="0 0 24 24" fill="none" stroke="#999" stroke-width="1.2"><path d="M3 17h18M5 17a7 7 0 0 1 14 0M12 8V6M2 20h20"/></svg></div><h3>HOSPITALITY INDUSTRY</h3><p>Lorem Ipsum is simply dummy text of the printing and typesetting industry. Lorem Ipsum has been the industry's standard dummy text ever since the 1500s.</p></div>
      <div class="topic"><div class="ico"><svg width="22" height="22" viewBox="0 0 24 24" fill="none" stroke="#999" stroke-width="1.2"><path d="M3 9l9-5 9 5zM5 9v9M9 9v9M15 9v9M19 9v9M3 20h18"/></svg></div><h3>BANKS, LOANS, FINANCING</h3><p>Lorem Ipsum is simply dummy text of the printing and typesetting industry. Lorem Ipsum has been the industry's standard dummy text ever since the 1500s.</p></div>
      <div class="topic"><div class="ico"><svg width="22" height="22" viewBox="0 0 24 24" fill="none" stroke="#999" stroke-width="1.2"><rect x="5" y="3" width="14" height="18"/><path d="M9 15l6-6M9 9h.01M15 15h.01"/></svg></div><h3>TAX PLANNING</h3><p>Lorem Ipsum is simply dummy text of the printing and typesetting industry. Lorem Ipsum has been the industry's standard dummy text ever since the 1500s.</p></div>
      <div class="topic"><div class="ico"><svg width="22" height="22" viewBox="0 0 24 24" fill="none" stroke="#999" stroke-width="1.2"><path d="M10 4l6 6-3 3-6-6zM11.5 11.5 4 19M14 20h7"/></svg></div><h3>NON- US LAW FIRMS</h3><p>Lorem Ipsum is simply dummy text of the printing and typesetting industry. Lorem Ipsum has been the industry's standard dummy text ever since the 1500s.</p></div>
    </div>
  </div>
</section>

<section class="advise">
  <div class="wrap">
    <div class="sec-head"><h2>WE CAN ADVISE ON WHATS MOST IMPORTANT TO YOU</h2><p>Lorem Ipsum is simply dummy text of the printing and typesetting industry.</p></div>
    <div class="need-grid">
      <div class="need"><svg width="50" height="48" viewBox="0 0 50 48" fill="none" stroke="#888" stroke-width="1.3"><rect x="4" y="4" width="18" height="42"/><path d="M22 22l12-8 12 8v24H22M8 10h4M14 10h4M8 18h4M14 18h4M8 26h4M14 26h4M31 46V34h7v12"/></svg><h3>US RESIDENCY</h3><p>Lorem Ipsum is simply dummy text of the printing and typesetting industry. Lorem Ipsum has been the industry's</p></div>
      <div class="need on"><svg width="60" height="48" viewBox="0 0 60 48" fill="none" stroke="#c1272d" stroke-width="1.5"><circle cx="30" cy="12" r="7"/><circle cx="14" cy="22" r="6"/><circle cx="46" cy="22" r="6"/><path d="M20 46V30a10 10 0 0 1 20 0v16M4 46V36a10 10 0 0 1 16 0M40 36a10 10 0 0 1 16 0v10"/></svg><h3>ADULT CHILDREN</h3><p>Lorem Ipsum is simply dummy text of the printing and typesetting industry. Lorem Ipsum has been the industry's</p></div>
      <div class="need"><svg width="50" height="48" viewBox="0 0 50 48" fill="none" stroke="#888" stroke-width="1.3"><circle cx="20" cy="14" r="9"/><circle cx="33" cy="18" r="8"/><path d="M4 44a16 16 0 0 1 32 0zM36 28a13 13 0 0 1 11 16"/></svg><h3>FAMILY MEMBERS</h3><p>Lorem Ipsum is simply dummy text of the printing and typesetting industry. Lorem Ipsum has been the industry's</p></div>
      <div class="need"><svg width="52" height="48" viewBox="0 0 52 48" fill="none" stroke="#888" stroke-width="1.4"><path d="M26 44 7 25A11 11 0 0 1 26 10a11 11 0 0 1 19 15z"/><path d="M9 25h10l3-6 4 12 4-8h13"/></svg><h3>HEALTHCARE</h3><p>Lorem Ipsum is simply dummy text of the printing and typesetting industry. Lorem Ipsum has been the industry's</p></div>
      <div class="need"><svg width="44" height="48" viewBox="0 0 44 48" fill="none" stroke="#888" stroke-width="1.3"><rect x="6" y="5" width="32" height="40"/><rect x="16" y="2" width="12" height="6"/><circle cx="22" cy="20" r="4"/><path d="M14 32a8 8 0 0 1 16 0zM12 38h20"/></svg><h3>ESTABLISHING CREDIT</h3><p>Lorem Ipsum is simply dummy text of the printing and typesetting industry. Lorem Ipsum has been the industry's</p></div>
      <div class="need"><svg width="50" height="48" viewBox="0 0 50 48" fill="none" stroke="#888" stroke-width="1.3"><path d="M16 20 30 8l14 12v16H16z"/><rect x="26" y="24" width="8" height="12"/><path d="M4 34h10l8 6h10M4 44h30l10-8"/><circle cx="12" cy="22" r="6"/><path d="M12 19v6"/></svg><h3>BUYING A HOME</h3><p>Lorem Ipsum is simply dummy text of the printing and typesetting industry. Lorem Ipsum has been the industry's</p></div>
    </div>
  </div>
</section>

<section class="feature">
  <div class="feature-photo" role="img" aria-label="Couple shaking hands with a consultant in a bright office"></div>
  <div class="feature-text">
    <h2>LOREM IPSUM IS SIMPLY DUMMY</h2>
    <p>Lorem Ipsum is simply dummy text of the printing and typesetting industry.<br>Lorem Ipsum has been the industry's standard dummy text ever since</p>
    <p>Lorem Ipsum is simply dummy text of the printing and typesetting industry. Lorem Ipsum has been the industry's standard dummy text ever since the 1500s, when an unknown printer took a galley of type and scrambled it to make a type specimen book. It has survived not only five centuries, but also the leap into electronic typesetting, remaining essentially unchanged. It was popularised in the 1960s with the release of Typeset sheets containing Lorem Ipsum passages,</p>
    <span class="btn-white">READ MORE</span>
  </div>
</section>

<section class="testimonials">
  <div class="wrap">
    <div class="sec-head"><h2>TESTIMONIALS</h2><p>Lorem Ipsum is simply dummy text of the printing and typesetting industry.</p></div>
    <div class="quote">
      <span class="qmark" style="left:-66px">&ldquo;</span>
      Lorem ipsum dolor sit amet, consectetuer adipiscing elit, sed diam nonummy nibh euismod tincidunt ut laoreet dolore magna aliquam erat volutpat. Ut wisi enim ad minim veniam, quis nostrud exerci tation ullamcorper suscipit lobortis nisl ut aliquipcommodo consequat vulputate esse molestie consequat
      <span class="qmark" style="right:-66px">&rdquo;</span>
    </div>
    <svg class="arrow" style="left:-28px" width="16" height="32" viewBox="0 0 16 32" fill="none" stroke="#888" stroke-width="1.4"><path d="M14 2 2 16l12 14"/></svg>
    <svg class="arrow" style="right:-28px" width="16" height="32" viewBox="0 0 16 32" fill="none" stroke="#888" stroke-width="1.4"><path d="M2 2l12 14L2 30"/></svg>
    <div class="author">
      <div class="avatar" role="img" aria-label="Client portrait"></div>
      <div><h4>LOREM IPSUM</h4><span>Lorem Ipsum is simply</span></div>
    </div>
  </div>
</section>

<section class="blogs">
  <div class="wrap">
    <div class="sec-head"><h2>LATEST BLOGS</h2><p>Lorem Ipsum is simply dummy text of the printing and typesetting industry.</p><div class="bar"></div></div>
    <div class="blog-grid">
      <article class="post"><div class="post-img" role="img" aria-label="US passport lying on a striped flag" style="background:linear-gradient(135deg,#d6323a 0%,#f1eeee 45%,#1f2a55 60%,#c9353b 100%)"></div><div class="post-date">16<small>FEB</small></div><h3>LOREM IPSUM DOLOR SIT AMET</h3><div class="meta"><span>&#9673; 542</span><span>&#9679; 17</span></div><p>Lorem Ipsum is simply dummy text of the printing and typesetting industry. Lorem Ipsum</p></article>
      <article class="post"><div class="post-img" role="img" aria-label="Scales of justice in a courtroom" style="background:linear-gradient(160deg,#3a2418 0%,#b26a30 55%,#6a3b1c 100%)"></div><div class="post-date">12<small>FEB</small></div><h3>LOREM IPSUM DOLOR SIT AMET</h3><div class="meta"><span>&#9673; 992</span><span>&#9679; 42</span></div><p>Lorem Ipsum is simply dummy text of the printing and typesetting industry. Lorem Ipsum</p></article>
      <article class="post"><div class="post-img" role="img" aria-label="Domed capitol building against a blue sky" style="background:linear-gradient(120deg,#7f7a6e 0%,#cfc8b8 45%,#2e5ea8 75%,#1c3f86 100%)"></div><div class="post-date">10<small>FEB</small></div><h3>LOREM IPSUM DOLOR SIT AMET</h3><div class="meta"><span>&#9673; 1560</span><span>&#9679; 98</span></div><p>Lorem Ipsum is simply dummy text of the printing and typesetting industry. Lorem Ipsum</p></article>
    </div>
  </div>
</section>

<footer class="site-footer">
  <div class="wrap" style="height:300px">
    <div class="fcol" style="left:0;width:204px"><h4>DISCLAIMER</h4><div class="rule"></div><p>Lorem Ipsum is simply dummy text of the printing and typesetting industry. Lorem Ipsum has been the industry's standard dummy text ever since the 1500s, when an unknown printer took a galley of type and scrambled it to make a type specimen book.</p></div>
    <div class="fcol" style="left:274px"><h4>QUICL LINK</h4><div class="rule"></div><ul class="links"><li>Home</li><li>About Us</li><li>Our Speciality</li><li>EB-5 Visa</li><li>Testimonials</li><li>Blog</li><li>Contact Us</li><li>Privacy Policy</li></ul></div>
    <div class="fcol" style="left:435px"><h4>GET IN TOUCH</h4><div class="rule" style="margin-bottom:12px"></div>
      <dl class="contact"><dt>Address:</dt><dd>Lorem Ipsum is simply dummy text of the printing</dd><dt>Phone:</dt><dd>+ 1555 014 2200</dd><dt>Email:</dt><dd>me@mbc.email</dd><dt style="border:0">Follow Us:</dt><dd style="border:0"><div class="follow"><span></span><span></span><span></span><span></span><span></span><span></span><span></span></div></dd></dl>
    </div>
    <div class="fcol" style="left:698px"><h4>SCHEDULE A CONSULTATION</h4><div class="rule"></div>
      <div class="field"><svg width="10" height="10" viewBox="0 0 10 10" fill="none" stroke="#aaa"><circle cx="5" cy="3" r="2.5"/><path d="M.5 10a4.5 4.5 0 0 1 9 0"/></svg>Name</div>
      <div class="field"><svg width="11" height="8" viewBox="0 0 11 8" fill="none" stroke="#aaa"><rect x=".5" y=".5" width="10" height="7"/><path d="M.5.5 5.5 5l5-4.5"/></svg>Email Address</div>
      <div class="field msg"></div>
      <span class="btn-send">Send Message</span>
    </div>
  </div>
  <div class="totop"><svg width="12" height="8" viewBox="0 0 12 8" fill="none" stroke="#fff" stroke-width="1.5"><path d="M1 7l5-5 5 5"/></svg></div>
</footer>
<div class="base">&copy; 2018, Meridian Bridge Consultants - All Rights Reserved</div>

</body>
</html>
```